Web Page needed for Dr. Wanbrook Consult

The company works in the consultant business for processes in large projects our of engineering and construction business. We develop strategies but work also in critical projects to get them right.
The page should have a modern appearance but though a classy and luxury touch.
Updates

The project was bought in a package, logo plus web page. Now the designers do submit logos again, although the logo has been set. This part is only the web site. I changed the text to clarify it, I contacted support to put that right, but that needs an extension of minimum 7 days to catch up.

Due to the confusion in the project, it was first set up as logo project and later corrected (I have no clue how that happened, as I bought a package with logo + web, and logo is already done), there is a large delay in getting feedback. Please be so kind and extend until 31.01. In Europe there is holidays until 07.01. and I have no time to discuss the topics with my client until 10.01., than we need to feed in response and get changes done.

Logo Text

The logo is already fixed, I asked for web page.

Number of Pages Required

5+ page

Font styles to use
Sans Serif

Colors

Designer to choose colors to be used in the design.

Requirements
Must have
• Home/Start
• Lean Construction
• Lean Equipment
• Lean Design
• Lean Training
• Team
• Contact
• Imprint
Nice to have
• Darker color, luxury appearance, please integrate the logo in the attachment here.
• I would like to have a web page with animated context, such as this one here: https://tovalmerworks.example

```html
<!DOCTYPE html>
<html lang="en">
<head>
<meta charset="utf-8">
<title>Wanbrook Consult</title>
<link rel="stylesheet" href="https://fonts.googleapis.com/css2?family=Nunito+Sans:wght@400;600;700;800&family=Poppins:wght@700;800&display=swap">
<style>
:root{
  --blue:#1d55b0;
  --blue-deep:#184a9c;
  --footer:#2a62bb;
  --ink:#141414;
  --text:#444;
  --line:#e4e4e4;
  --white:#fff;
  --photo-warm:linear-gradient(160deg,#8a6a52,#c9763a 55%,#5a4a3f);
}
*{margin:0;padding:0;box-sizing:border-box}
html,body{width:1200px;height:3895px;overflow:hidden;background:var(--white)}
body{position:relative;font-family:"Nunito Sans",Arial,sans-serif;color:var(--ink)}
.abs{position:absolute}
a{color:inherit;text-decoration:none}

/* header */
.site-header{position:absolute;left:0;top:0;width:1200px;height:88px;background:var(--white)}
.brand{position:absolute;left:89px;top:24px;display:flex;align-items:center;gap:10px;font-weight:800;font-size:18px;color:var(--blue-deep)}
.brand .mark{width:34px;height:34px;background:var(--blue-deep)}
.main-nav{position:absolute;left:305px;top:34px;display:flex;gap:16px;font-size:13.5px;font-weight:600;white-space:nowrap}
.main-nav .active{color:var(--blue)}
.social-top{position:absolute;left:992px;top:35px;display:flex;gap:20px}
.social-top span{width:15px;height:15px;border-radius:50%;background:var(--ink)}

/* hero */
.hero{position:absolute;left:0;top:88px;width:1200px;height:820px}
.hero h1{position:absolute;left:0;top:293px;width:1200px;text-align:center;font-family:Poppins,Arial,sans-serif;font-weight:800;font-size:52px;line-height:59px;color:var(--white);text-transform:uppercase}

/* dividers */
.divider{position:absolute;left:89px;width:1022px;height:1px;background:var(--line)}
.divider i{position:absolute;top:-1px;height:2px;background:var(--blue)}

/* text blocks */
.eyebrow{font-size:21px;font-weight:600}
.section-title{font-size:38px;line-height:48px;font-weight:700}
.copy{font-size:13.5px;line-height:22.4px;color:var(--text)}
.round-btn{width:34px;height:34px;border-radius:50%;background:var(--blue);display:flex;align-items:center;justify-content:center}
.learn{color:var(--blue);font-weight:700;font-size:15.5px}

/* news */
.card{position:absolute;top:2853px;width:322px;height:357px;background:var(--white);box-shadow:0 4px 14px rgba(0,0,0,.1)}
.card .pic{height:158px}
.card .date{position:absolute;left:16px;top:150px;background:var(--blue);color:var(--white);font-weight:700;font-size:14px;padding:3px 22px}
.card h3{position:absolute;left:17px;top:196px;width:290px;font-size:19px;line-height:22px;font-weight:700}
.card p{position:absolute;left:17px;top:256px;width:290px;font-size:12px;line-height:19.5px;color:var(--text)}
.card .more{position:absolute;left:26px;top:324px;font-size:12.5px;color:var(--blue);font-weight:600;display:flex;gap:8px;align-items:center}

/* partners */
.partner{position:absolute;top:3332px;width:197px;height:76px;border:1px solid var(--line);display:flex;align-items:center;justify-content:center}
.partner span{width:40px;height:40px;border-radius:50%;background:#d4d4d4}

/* footer */
.footer-shape{position:absolute;left:0;top:3470px}
.footer-brand{position:absolute;left:89px;top:3670px;display:flex;align-items:center;gap:10px;color:var(--white);font-weight:800;font-size:18px}
.footer-brand .mark{width:34px;height:34px;background:var(--white)}
.footer-col{position:absolute;top:3613px;color:var(--white)}
.footer-col h4{font-size:15.5px;font-weight:600;letter-spacing:.3px;margin-bottom:14px}
.footer-col li{list-style:none;font-size:12px;line-height:29px;opacity:.92}
.contact-row{display:flex;gap:10px;font-size:12px;line-height:22px;margin-bottom:10px}
.contact-row svg{margin-top:4px;flex:none}
.footer-social{position:absolute;left:89px;top:3752px;display:flex;gap:12px}
.footer-social span{width:30px;height:30px;border-radius:50%;background:rgba(255,255,255,.18)}
.copyright{position:absolute;left:0;top:3861px;width:1200px;text-align:center;color:var(--white);font-size:11.5px}
.to-top{position:absolute;left:1137px;top:3826px;width:34px;height:34px;border-radius:50%;background:var(--white);display:flex;align-items:center;justify-content:center}
</style>
</head>
<body>

<header class="site-header">
  <a class="brand" href="#"><span class="mark"></span>Wanbrook Consult</a>
  <nav class="main-nav">
    <a class="active" href="#">Home</a><a href="#">Lean Construction</a><a href="#">Lean Equipment</a><a href="#">Lean Design</a><a href="#">Lean Training</a><a href="#">Team</a><a href="#">Contact</a><a href="#">Imprint</a>
  </nav>
  <div class="social-top"><span></span><span></span><span></span><span></span></div>
</header>

<section class="hero">
  <svg width="1200" height="820" role="img" aria-label="Smiling construction engineer in hard hat and orange vest holding a tablet in front of a building site">
    <defs><linearGradient id="heroGrad" x1="0" y1="0" x2="1" y2="1"><stop offset="0" stop-color="#6f5a4a"/><stop offset=".5" stop-color="#c8692c"/><stop offset="1" stop-color="#4a3d35"/></linearGradient></defs>
    <polygon fill="url(#heroGrad)" points="0,0 1200,0 1200,358 1105,403 1105,637 1002,699 902,645 397,818 95,637 95,532 0,471"/>
  </svg>
  <h1>We help you to grow<br>your business</h1>
</section>

<div class="divider" style="top:976px"><i style="left:0;width:308px"></i></div>

<section class="about">
  <div class="abs" role="img" aria-label="Smiling engineer in orange vest holding a white hard hat" style="left:88px;top:1055px;width:453px;height:429px;background:var(--photo-warm)"></div>
  <svg class="abs" style="left:393px;top:1484px" width="30" height="22"><polygon points="0,0 30,0 15,20" fill="#e8581c"/></svg>
  <p class="abs eyebrow" style="left:612px;top:1110px">About Us</p>
  <h2 class="abs section-title" style="left:612px;top:1138px">Welcome To Our<br>Company</h2>
  <p class="abs copy" style="left:612px;top:1246px;width:475px">Nemo enim ipsam voluptatem quia voluptas sit aspernatur aut odit aut fugit, sed quia consequuntur magni dolores eos qui ratione voluptatem sequi nesciunt. Neque porro quisquam est, qui dolorem ipsum quia dolor sit amet, consectetur, adipisci velit, sed quia non numquam eius modi tempora incidunt ut labore et dolore magnam aliquam quaerat voluptatem. Ut enim ad minima veniam...</p>
  <div class="abs" style="left:612px;top:1410px;display:flex;align-items:center;gap:17px">
    <span class="round-btn"><svg width="14" height="12"><path d="M1 6h11M7 1l5 5-5 5" stroke="#fff" stroke-width="2" fill="none"/></svg></span>
    <span class="learn">Learn More</span>
  </div>
</section>

<div class="divider" style="top:1580px"><i style="left:284px;width:311px"></i></div>

<section class="work">
  <p class="abs eyebrow" style="left:90px;top:1739px">What We Do</p>
  <h2 class="abs section-title" style="left:90px;top:1769px">Some Of Our Recent<br>Work.</h2>
  <h3 class="abs" style="left:90px;top:1892px;font-size:21px;font-weight:600">London Residential Works</h3>
  <p class="abs copy" style="left:90px;top:1921px;width:475px">Nemo enim ipsam voluptatem quia voluptas sit aspernatur aut odit aut fugit, sed quia consequuntur magni dolores eos qui ratione voluptatem sequi nesciunt. Neque porro quisquam est, qui dolorem ipsum quia dolor sit amet, consectetur, adipisci velit, sed quia non numquam eius modi tempora incidunt ut labore et dolore magnam aliquam quaerat voluptatem. Ut enim ad minima veniam, quis nostrum exercitationem ullam corporis suscipit laboriosam...</p>
  <div class="abs" style="left:90px;top:2099px;display:flex;gap:19px">
    <span class="round-btn"><svg width="14" height="12"><path d="M13 6H2M7 1 2 6l5 5" stroke="#fff" stroke-width="2" fill="none"/></svg></span>
    <span class="round-btn"><svg width="14" height="12"><path d="M1 6h11M7 1l5 5-5 5" stroke="#fff" stroke-width="2" fill="none"/></svg></span>
  </div>
  <svg class="abs" style="left:632px;top:1652px" width="478" height="575" role="img" aria-label="Three engineers in hard hats reviewing plans at a high-rise construction site">
    <defs><linearGradient id="workGrad" x1="0" y1="0" x2="1" y2="1"><stop offset="0" stop-color="#8e979f"/><stop offset=".6" stop-color="#d98530"/><stop offset="1" stop-color="#4f5b66"/></linearGradient></defs>
    <polygon fill="url(#workGrad)" points="22,0 478,0 478,575 22,575 22,312 0,290 22,268"/>
  </svg>
  <svg class="abs" style="left:89px;top:2276px" width="310" height="366" role="img" aria-label="Engineers with tablet inside a concrete building under construction"><polygon fill="#7d8791" points="0,0 296,0 296,163 310,183 296,203 296,366 0,366"/></svg>
  <svg class="abs" style="left:446px;top:2276px" width="310" height="366" role="img" aria-label="Two engineers talking in front of a building frame"><polygon fill="#a4794f" points="0,0 296,0 296,163 310,183 296,203 296,366 0,366"/></svg>
  <svg class="abs" style="left:802px;top:2276px" width="310" height="366" role="img" aria-label="Three engineers reading a clipboard on site"><polygon fill="#8f8477" points="0,0 296,0 296,163 310,183 296,203 296,366 0,366"/></svg>
</section>

<div class="divider" style="top:2714px"><i style="left:712px;width:310px"></i></div>

<section class="news">
  <h2 class="abs" style="left:91px;top:2775px;font-size:40px;font-weight:700">Latest News</h2>
  <article class="card" style="left:91px">
    <div class="pic" role="img" aria-label="Team joining fists together seen from below" style="background:linear-gradient(160deg,#e9e9e9,#6b6f74 60%,#2e2f33)"></div>
    <span class="date">18.02.16</span>
    <h3>Nor again is there anyone who Lorem ipsum</h3>
    <p>"Lorem ipsum dolor sit amet, consectetur adipiscing elit, sed do eiusmod tempor incididunt ut labore et dolore...</p>
    <a class="more" href="#">Read More <svg width="12" height="10"><path d="M0 5h10M6 1l4 4-4 4" stroke="#1d55b0" stroke-width="1.6" fill="none"/></svg></a>
  </article>
  <article class="card" style="left:438px">
    <div class="pic" role="img" aria-label="Construction workers in hard hats sitting on a bench" style="background:linear-gradient(160deg,#7a5a44,#e08a2a 55%,#3c4f6e)"></div>
    <span class="date">18.02.16</span>
    <h3>Nor again is there anyone who Lorem ipsum</h3>
    <p>"Lorem ipsum dolor sit amet, consectetur adipiscing elit, sed do eiusmod tempor incididunt ut labore et dolore...</p>
    <a class="more" href="#">Read More <svg width="12" height="10"><path d="M0 5h10M6 1l4 4-4 4" stroke="#1d55b0" stroke-width="1.6" fill="none"/></svg></a>
  </article>
  <article class="card" style="left:787px">
    <div class="pic" role="img" aria-label="Two colleagues working together in a bright office" style="background:linear-gradient(160deg,#ecebe8,#c9a98e 50%,#e2c53a)"></div>
    <span class="date">18.02.16</span>
    <h3>Nor again is there anyone who Lorem ipsum</h3>
    <p>"Lorem ipsum dolor sit amet, consectetur adipiscing elit, sed do eiusmod tempor incididunt ut labore et dolore...</p>
    <a class="more" href="#">Read More <svg width="12" height="10"><path d="M0 5h10M6 1l4 4-4 4" stroke="#1d55b0" stroke-width="1.6" fill="none"/></svg></a>
  </article>
</section>

<div class="divider" style="top:3287px"><i style="left:357px;width:310px"></i></div>

<section class="partners">
  <div class="partner" style="left:89px"><span></span></div>
  <div class="partner" style="left:295px"><span></span></div>
  <div class="partner" style="left:501px"><span></span></div>
  <div class="partner" style="left:708px"><span></span></div>
  <div class="partner" style="left:914px"><span></span></div>
</section>

<footer class="site-footer">
  <svg class="footer-shape" width="1200" height="425"><polygon fill="var(--footer)" points="0,172 193,66 295,126 400,66 600,66 751,5 1111,5 1111,172 1200,157 1200,425 0,425"/></svg>
  <div class="footer-brand"><span class="mark"></span>Wanbrook Consult</div>
  <div class="footer-social"><span></span><span></span><span></span><span></span></div>
  <div class="footer-col" style="left:456px">
    <h4>QUICK LINKS</h4>
    <ul><li>Home</li><li>Lean Construction</li><li>Lean Design</li><li>Team</li><li>Contact</li></ul>
  </div>
  <div class="footer-col" style="left:678px">
    <h4>INFORMATION</h4>
    <ul><li>Terms &amp; Condition</li><li>Privacy Policy</li><li>Site Map</li><li>Disclaimer</li><li>Imprint</li></ul>
  </div>
  <div class="footer-col" style="left:902px">
    <h4>CONTACT INFO</h4>
    <div class="contact-row"><svg width="13" height="10"><rect width="13" height="10" rx="1" fill="#fff"/><path d="M0 1l6.5 5L13 1" stroke="#2a62bb" fill="none"/></svg><div>Email:<br>info@wanbrook.example</div></div>
    <div class="contact-row"><svg width="13" height="13"><path d="M3 1l3 3-2 2c1 2 2 3 4 4l2-2 3 3-2 2C6 13 0 7 1 3z" fill="#fff"/></svg><div>Phone:<br>123.45 Lorem Ipsum</div></div>
    <div class="contact-row"><svg width="11" height="14"><path d="M5.5 0A5.5 5.5 0 0 0 0 5.5C0 9 5.5 14 5.5 14S11 9 11 5.5A5.5 5.5 0 0 0 5.5 0z" fill="#fff"/><circle cx="5.5" cy="5.5" r="2" fill="#2a62bb"/></svg><div>Location:<br>Some adress line goes here...</div></div>
  </div>
  <p class="copyright">© Wanbrook Consult Ltd. All rights reserved.</p>
  <a class="to-top" href="#"><svg width="10" height="12"><path d="M5 12V1M1 5l4-4 4 4" stroke="#1d55b0" stroke-width="1.4" fill="none"/></svg></a>
</footer>

</body>
</html>
```